Farm product labels

This is meant to design a set of labels for the following products:
Sachets (similar to Brindlecombe’s ketchup):
- Size: W4xH9 cm. This is the internal area (inside the four sealing borders) of sachets. Front side contains the design, and back side just texts with the ingredients, nutrition facts and origin. Please check check the attached pictures related to sachet designs for your reference!
- Products:
o Ketchup
o Honey
o Dulcevara (chocolate spread made of cacao, peanuts, and milk)
o Peanut butter
o Fruit jam (either Mango, Guava or Passion fruit)

Stickers (to be added on transparent bags):
- Size: W8xH14 cm. It does not need to be rectangular
- It needs to accommodate small texts with the ingredients, nutrition facts and origin
- Products:
o Tomato paste
o Fruit pulp (either Mango, Guava or Passion fruit)
o Processed vegetables (either Yuca or Sweet potato). They are peeled, chopped, pre-boiled and frozen.

For those interested I’ll provide detailed info as required

Target Market(s)

Hotels. The sachets are specially for breakfast

Requirements
Must have
• All product label designs should:
- Show a similar look, reflecting a single source/branding
- Be attractive and be easy to recognize each product
- Contain the logo of our farm (uploaded)

```html
<!DOCTYPE html>
<html lang="en">
<head>
<meta charset="utf-8">
<title>Ketchup Sachet Labels – Finca Valdemora</title>
<link href="https://fonts.googleapis.com/css2?family=Barlow+Condensed:wght@500;600;700;800&family=Barlow+Semi+Condensed:wght@400&display=swap" rel="stylesheet">
<style>
  :root {
    --stage: #3a3a3c;
    --sachet-red: #e61e27;
    --band-white: #ffffff;
    --brand-blue: #1f3f94;
    --tomato-red: #d8232a;
    --tomato-light: #f26a55;
    --text-white: #ffffff;
  }
  * { margin: 0; padding: 0; box-sizing: border-box; }
  html, body {
    width: 1160px;
    height: 1200px;
    overflow: hidden;
    background: var(--stage);
  }
  .label-sheet {
    position: relative;
    width: 1160px;
    height: 1200px;
  }
  .sachet {
    position: absolute;
    top: 133px;
    width: 416px;
    height: 934px;
    background: var(--sachet-red);
    overflow: hidden;
  }
  .sachet--front { left: 133px; }
  .sachet--back { left: 612px; }

  .sachet__band {
    position: absolute;
    inset: 0;
    width: 416px;
    height: 934px;
  }

  .product-title {
    position: absolute;
    left: 0;
    right: 0;
    top: 116px;
    text-align: center;
    color: var(--text-white);
    font-family: "Barlow Condensed", sans-serif;
    font-weight: 800;
    font-size: 78px;
    line-height: 1;
    letter-spacing: 0.5px;
  }
  .product-variant {
    position: absolute;
    left: 0;
    right: 0;
    top: 190px;
    text-align: center;
    color: var(--text-white);
    font-family: "Barlow Condensed", sans-serif;
    font-weight: 700;
    font-size: 42px;
    line-height: 1;
  }

  .brand-mark {
    position: absolute;
    display: flex;
    align-items: center;
    justify-content: center;
    text-align: center;
    color: var(--brand-blue);
    font-family: "Barlow Condensed", sans-serif;
    font-weight: 700;
    text-transform: uppercase;
    line-height: 1.05;
    letter-spacing: 1px;
  }
  .sachet--front .brand-mark {
    left: 59px; top: 287px; width: 298px; height: 298px;
    font-size: 44px;
  }
  .sachet--back .brand-mark {
    left: 88px; top: 277px; width: 238px; height: 238px;
    font-size: 36px;
  }

  .tomato-visual {
    position: absolute;
    left: 28px;
    top: 650px;
    width: 356px;
    height: 245px;
    border-radius: 50% 50% 46% 46%;
    background: radial-gradient(ellipse at 40% 45%, var(--tomato-light) 0%, var(--tomato-red) 55%, #b5161d 100%);
  }

  .info-heading {
    position: absolute;
    left: 0;
    right: 0;
    top: 536px;
    text-align: center;
    color: var(--text-white);
    font-family: "Barlow Condensed", sans-serif;
    font-weight: 600;
    font-size: 44px;
    line-height: 1;
  }
  .info-body {
    position: absolute;
    left: 20px;
    right: 20px;
    top: 587px;
    text-align: center;
    color: var(--text-white);
    font-family: "Barlow Semi Condensed", sans-serif;
    font-weight: 400;
    font-size: 26.5px;
    line-height: 33px;
  }
</style>
</head>
<body>
<main class="label-sheet">

  <section class="sachet sachet--front">
    <svg class="sachet__band" viewBox="0 0 416 934" aria-hidden="true">
      <polygon points="0,381 416,291 416,419 0,508" fill="var(--band-white)"/>
      <circle cx="208" cy="436" r="149" fill="var(--band-white)"/>
    </svg>
    <h1 class="product-title">KETCHUP</h1>
    <p class="product-variant">cuban blend</p>
    <div class="brand-mark">Finca<br>Valdemora</div>
    <div class="tomato-visual" role="img" aria-label="Whole ripe tomato with green stem beside a halved tomato"></div>
  </section>

  <section class="sachet sachet--back">
    <svg class="sachet__band" viewBox="0 0 416 934" aria-hidden="true">
      <polygon points="0,291 416,358 416,485 0,420" fill="var(--band-white)"/>
      <circle cx="207" cy="396" r="119" fill="var(--band-white)"/>
    </svg>
    <div class="brand-mark">Finca<br>Valdemora</div>
    <h2 class="info-heading">LOREM IPSUM</h2>
    <p class="info-body">Lorem ipsum dolor sit amet, consectetuer adipiscing elit, sed diam nonummy nibh euismod tincidunt ut laoreet dolore magna aliquam erat volutpat. Ut wisi enim ad minim veniam, quis nostrud exerci tation ullamcorper suscipit lobortis nisl ut</p>
  </section>

</main>
</body>
</html>
```